Meadowbrook Yard Care Partial Truck Wrap Design

We're a lawn care company looking for a modern partial truck wrap for our vehicles. We already have the media and contact info, as well as some references I would like our wrap to be similar to. I can provide contact info once a design is close to being finalized. Let me know if any other info is needed for the project. I have attached our truck, our logo, our character, and our website is contact@meadowbrookyardcare.example. Green, Red (#bd0f03), and White are our colors, but feel free to use other colors that fit, I think brown or black would be fine aswell if it fits.

```html
<!DOCTYPE html>
<html lang="en">
<head>
<meta charset="utf-8">
<title>Meadowbrook Yard Care – Partial Truck Wrap</title>
<link rel="stylesheet" href="https://fonts.googleapis.com/css2?family=Montserrat:wght@500;800&display=swap">
<style>
  :root {
    --wrap-green: #3fae49;
    --wrap-green-dark: #2f8f3a;
    --wrap-red: #d33a2c;
    --brand-red: #bd0f03;
    --text-white: #ffffff;
    --tire: #1d1d1d;
    --glass: #3b4148;
    --rim: #b9bcbf;
    --page: #f2f2f2;
    --divider: #c9c9c9;
  }
  * { margin: 0; padding: 0; box-sizing: border-box; }
  html, body { width: 1200px; height: 854px; overflow: hidden; background: var(--page); }
  .canvas { position: relative; width: 1200px; height: 854px; font-family: "Montserrat", sans-serif; }
  .side-view { position: absolute; left: 0; width: 1200px; height: 427px; }
  .side-view--driver { top: 0; }
  .side-view--passenger { top: 427px; border-top: 1px solid var(--divider); }
  .truck-shape { position: absolute; inset: 0; width: 1200px; height: 427px; }
  .truck-shape--mirrored { transform: scaleX(-1); }

  .brand-name {
    position: absolute; width: 290px;
    color: var(--text-white); font-weight: 800; font-size: 31px;
    line-height: 1.1; text-transform: uppercase; text-align: center; letter-spacing: 1px;
  }
  .mascot-area {
    position: absolute; width: 120px; height: 150px; border-radius: 10px;
    background: linear-gradient(180deg, #b88a5a 0%, #c9463a 100%);
  }
  .contact { position: absolute; color: var(--text-white); }
  .contact__phone { font-weight: 800; font-size: 25px; letter-spacing: 1px; }
  .contact__email { font-weight: 500; font-size: 10.5px; margin-top: 2px; }

  .side-view--driver .brand-name { left: 365px; top: 180px; }
  .side-view--driver .mascot-area { left: 665px; top: 130px; }
  .side-view--driver .contact { left: 830px; top: 128px; }
  .side-view--passenger .brand-name { left: 540px; top: 180px; }
  .side-view--passenger .mascot-area { left: 412px; top: 130px; }
  .side-view--passenger .contact { left: 185px; top: 128px; }
</style>
</head>
<body>
<main class="canvas">

  <svg width="0" height="0" style="position:absolute">
    <defs>
      <clipPath id="truck-body">
        <path d="M128,150 L140,135 Q200,118 330,112 L420,40 Q450,28 600,30 L620,120 L1080,125 L1085,270 L1020,272 Q1005,192 890,195 Q800,200 790,290 L330,295 Q325,228 250,225 Q175,222 165,300 L130,290 Z"/>
      </clipPath>
      <g id="truck-profile">
        <g clip-path="url(#truck-body)">
          <rect x="100" y="0" width="1000" height="320" fill="var(--wrap-green)"/>
          <rect x="355" y="0" width="285" height="320" fill="var(--wrap-red)"/>
        </g>
        <path d="M410,112 L468,56 L580,56 L584,126 Z" fill="var(--glass)"/>
        <line x1="590" y1="40" x2="592" y2="290" stroke="#8a2a20" stroke-width="2"/>
        <rect x="1055" y="150" width="30" height="55" rx="4" fill="var(--brand-red)"/>
        <circle cx="250" cy="298" r="68" fill="var(--tire)"/>
        <circle cx="250" cy="298" r="42" fill="var(--rim)"/>
        <circle cx="890" cy="292" r="68" fill="var(--tire)"/>
        <circle cx="890" cy="292" r="42" fill="var(--rim)"/>
      </g>
    </defs>
  </svg>

  <section class="side-view side-view--driver">
    <svg class="truck-shape" viewBox="0 0 1200 427" aria-hidden="true"><use href="#truck-profile"/></svg>
    <p class="brand-name">Meadowbrook<br>Yard Care</p>
    <div class="mascot-area" role="img" aria-label="Mascot character waving a foam finger"></div>
    <div class="contact">
      <p class="contact__phone">555 014 2290</p>
      <p class="contact__email">contact@meadowbrookyardcare.example</p>
    </div>
  </section>

  <section class="side-view side-view--passenger">
    <svg class="truck-shape truck-shape--mirrored" viewBox="0 0 1200 427" aria-hidden="true"><use href="#truck-profile"/></svg>
    <div class="contact">
      <p class="contact__phone">555 014 2290</p>
      <p class="contact__email">contact@meadowbrookyardcare.example</p>
    </div>
    <div class="mascot-area" role="img" aria-label="Mascot character waving a foam finger"></div>
    <p class="brand-name">Meadowbrook<br>Yard Care</p>
  </section>

</main>
</body>
</html>
```